BLUE HAVEN (Business Card for Training Company)

Blue Haven is a training and consultancy company with a focus on executive protection and medical. I would like the card to be nice and sharp, not overdone and in black and red. I would also like it to highlight that it is "A Dravin Company"

I would like it to be simple and highlight a few things.

1. Name
2. Title
3. Phone Number
4. Email

I would also like www.dravinholdings.example/blue-haven to be on the card somewhere.

Target Market(s)

Security Companies

Industry/Entity Type

Security

Contact Information for Business Card

Blue Haven is a training and consultancy company with a focus on executive protection and medical. I would like the card to be nice and sharp, not overdone and in black and red. I would also like it to highlight that it is "A Dravin Company" I would like it to be simple and highlight a few things. 1. Name 2. Title 3. Phone Number 4. Email I would also like www.dravinholdings.example/blue-haven to be on the card somewhere.

Requirements
Must have
• A Dravin Company listed on the card and the website
Nice to have
• Highlight Medical Training, Consultancy & Executive Protection Courses

```html
<!DOCTYPE html>
<html lang="en">
<head>
<meta charset="utf-8">
<title>Blue Haven Business Card</title>
<link href="https://fonts.googleapis.com/css2?family=Michroma&family=Open+Sans:ital,wght@0,400;0,600;0,800;1,400&display=swap" rel="stylesheet">
<style>
  :root {
    --bg: #e9e6e1;
    --card: #ffffff;
    --ink: #000000;
    --text: #333333;
    --maroon: #650000;
    --rule: #111111;
  }
  * { margin: 0; padding: 0; box-sizing: border-box; }
  html, body { width: 1200px; height: 1020px; overflow: hidden; background: var(--bg); }
  body { font-family: "Open Sans", sans-serif; color: var(--text); position: relative; }

  .card {
    position: absolute;
    left: 250px;
    width: 700px;
    height: 400px;
    background: var(--card);
    border-radius: 0 60px 0 60px;
    box-shadow: 0 6px 18px rgba(0,0,0,0.18);
    overflow: hidden;
  }
  .card--front { top: 80px; }
  .card--back { top: 540px; }

  .brand { position: absolute; }
  .brand-name {
    font-family: "Open Sans", sans-serif;
    font-weight: 800;
    color: var(--maroon);
    text-transform: uppercase;
    line-height: 0.95;
    letter-spacing: 1px;
  }
  .brand-parent {
    font-size: 13px;
    font-weight: 600;
    letter-spacing: 3px;
    text-transform: uppercase;
    color: var(--ink);
    margin-top: 8px;
  }

  .card--front .brand {
    left: 0; right: 0; top: 100px;
    text-align: center;
  }
  .card--front .brand-name { font-size: 64px; }
  .card--front .brand-parent { font-size: 15px; margin-top: 12px; }

  .website {
    position: absolute;
    left: 0; right: 0; bottom: 48px;
    text-align: center;
    font-size: 16px;
    letter-spacing: 4px;
    color: var(--text);
  }

  .name-band {
    position: absolute;
    left: 0; top: 22px;
    width: 330px; height: 104px;
  }
  .person { position: absolute; left: 60px; top: 48px; color: #fff; }
  .person-name {
    font-family: "Michroma", sans-serif;
    font-size: 15px;
    letter-spacing: 4px;
  }
  .person-title { font-size: 11px; margin-top: 1px; }

  .card--back .brand {
    right: 60px; top: 60px;
    text-align: left;
  }
  .card--back .brand-name { font-size: 42px; }
  .card--back .brand-parent { font-size: 11px; margin-top: 6px; }

  .divider {
    position: absolute;
    left: 20px; right: 40px; top: 178px;
    height: 1px;
    background: var(--rule);
  }

  .contacts { position: absolute; left: 28px; top: 198px; list-style: none; }
  .contacts li {
    display: flex; align-items: center;
    height: 30px;
    font-size: 14px; font-style: italic;
  }
  .contacts svg { width: 22px; height: 22px; margin-right: 14px; flex: none; }

  .address {
    position: absolute;
    right: 40px; top: 270px;
    font-size: 17px;
    line-height: 1.25;
  }

  .accent-band {
    position: absolute;
    left: 0; bottom: 36px;
    width: 620px; height: 22px;
  }
</style>
</head>
<body>

<section class="card card--front" aria-label="Card front">
  <div class="brand">
    <div class="brand-name">Blue<br>Haven</div>
    <p class="brand-parent">A Dravin Company</p>
  </div>
  <p class="website">www.dravinholdings.example/blue-haven</p>
</section>

<section class="card card--back" aria-label="Card back">
  <svg class="name-band" viewBox="0 0 330 104" aria-hidden="true">
    <polygon points="0,0 305,0 330,104 0,104" fill="var(--ink)"/>
  </svg>
  <div class="person">
    <p class="person-name">ALAN MERCER</p>
    <p class="person-title">CEO/Managing Director</p>
  </div>

  <div class="brand">
    <div class="brand-name">Blue<br>Haven</div>
    <p class="brand-parent">A Dravin Company</p>
  </div>

  <div class="divider"></div>

  <ul class="contacts">
    <li>
      <svg viewBox="0 0 22 22" aria-label="Phone">
        <circle cx="11" cy="11" r="11" fill="var(--maroon)"/>
        <path d="M8 6c-1 1-1.5 2-1 3.5 1 2.5 2.8 4.3 5.3 5.5 1.5.6 2.5 0 3.5-1l-1.8-1.8-1.4.8c-1.3-.6-2.3-1.6-3-3l.8-1.4z" fill="#fff"/>
      </svg>
      555-014-2288
    </li>
    <li>
      <svg viewBox="0 0 22 22" aria-label="Office">
        <circle cx="11" cy="11" r="11" fill="var(--maroon)"/>
        <path d="M11 5l-6 5.5h1.8V16h3v-3.5h2.4V16h3v-5.5H17z" fill="#fff"/>
      </svg>
      555-014-2288
    </li>
    <li>
      <svg viewBox="0 0 22 22" aria-label="Email">
        <circle cx="11" cy="11" r="11" fill="var(--maroon)"/>
        <rect x="5" y="7" width="12" height="8" fill="#fff"/>
        <path d="M5 7l6 4.5L17 7" fill="none" stroke="var(--maroon)" stroke-width="1"/>
      </svg>
      alanmercer@mailbox.example
    </li>
  </ul>

  <p class="address">118 Larkfield Road Suite 400<br>Eastbrook MI 49000</p>

  <svg class="accent-band" viewBox="0 0 620 22" aria-hidden="true">
    <polygon points="0,0 620,0 596,22 0,22" fill="var(--maroon)"/>
  </svg>
</section>

</body>
</html>
```